VelnoriCore Business Cards

Will need a front and back design for a business card for VelnoriCore.
Can accept the final product as an illustrator file.
www.velnoricore-example.com is the company website.

Target Market(s)

he target market are Chief Technology Officers and people in the tech field.

Industry/Entity Type

Business

Requirements
Must have
• - The business card must have on one of the sides
name
title
company
phone
email
website
The other side may be of some design, derivation of logo and or colors

```html
<!DOCTYPE html>
<html lang="en">
<head>
<meta charset="utf-8">
<title>VelnoriCore Business Cards</title>
<link rel="stylesheet" href="https://fonts.googleapis.com/css2?family=Source+Sans+3:wght@400;600;700&display=swap">
<style>
  :root {
    --navy-deep: #141f5e;
    --navy: #1b2f7e;
    --blue: #1d4f9c;
    --paper: #eef0f3;
    --paper-shade: #d7dbe1;
    --steel: #8d939b;
    --stripe: #a9aeb5;
    --white: #ffffff;
    --backdrop: #e4e6ea;
  }
  * { box-sizing: border-box; margin: 0; padding: 0; }
  html, body { width: 1200px; height: 880px; overflow: hidden; }
  body {
    background: var(--backdrop);
    font-family: "Source Sans 3", "Myriad Pro", sans-serif;
    position: relative;
  }
  .card {
    position: absolute;
    width: 540px;
    height: 309px;
    overflow: hidden;
    box-shadow: 0 10px 26px rgba(20, 31, 94, 0.22);
  }

  /* Front side */
  .card--front { left: 50px; top: 420px; background: var(--navy); }
  .front__head {
    position: absolute; left: 0; top: 0; width: 100%; height: 128px;
    background: linear-gradient(180deg, var(--white) 0%, var(--paper) 55%, var(--paper-shade) 100%);
  }
  .front__stripe {
    position: absolute; left: 0; top: 128px; width: 100%; height: 8px;
    background: var(--stripe);
  }
  .front__body {
    position: absolute; left: 0; top: 136px; width: 100%; height: 173px;
    background: linear-gradient(100deg, var(--navy-deep) 0%, var(--navy) 45%, var(--blue) 100%);
    color: var(--white);
  }
  .brand { position: absolute; left: 36px; top: 30px; display: flex; align-items: center; gap: 16px; }
  .brand__dot { width: 64px; height: 64px; border-radius: 50%; background: var(--navy); }
  .brand__name { font-size: 40px; font-weight: 700; color: var(--navy); line-height: 1; }
  .brand__tagline {
    font-size: 15px; font-weight: 600; letter-spacing: 2.4px; color: var(--steel);
    text-transform: uppercase; margin-top: 4px;
  }
  .person { position: absolute; left: 30px; top: 18px; }
  .person__name { font-size: 24px; font-weight: 700; }
  .person__title { font-size: 16px; font-weight: 400; opacity: 0.9; }
  .front__web { position: absolute; left: 30px; bottom: 20px; font-size: 15px; }
  .front__web b { font-weight: 700; }
  .divider {
    position: absolute; left: 282px; top: 16px; width: 2px; height: 140px;
    background: var(--white);
  }
  .contact { position: absolute; left: 300px; top: 16px; font-size: 15px; line-height: 1.35; }
  .contact__company { font-weight: 700; font-size: 16px; }
  .contact__lines { margin-top: 18px; }
  .contact__row { display: flex; align-items: center; gap: 8px; }
  .contact__row svg { flex: none; }

  /* Back side */
  .card--back {
    left: 610px; top: 150px;
    background: linear-gradient(135deg, var(--navy-deep) 0%, var(--navy) 45%, var(--blue) 100%);
    color: var(--white);
  }
  .back__circle {
    position: absolute; right: -60px; top: 60px; width: 260px; height: 260px;
    border-radius: 50%; background: rgba(255, 255, 255, 0.12);
  }
  .back__brand { position: absolute; left: 34px; top: 92px; }
  .back__name { font-size: 48px; font-weight: 700; line-height: 1; }
  .back__tagline {
    font-size: 16px; font-weight: 600; letter-spacing: 2.6px; text-transform: uppercase;
    margin-top: 6px;
  }
  .back__rule { width: 300px; height: 2px; background: var(--white); margin-top: 10px; }
  .back__web { font-size: 15px; letter-spacing: 1.2px; margin-top: 8px; }
</style>
</head>
<body>

  <section class="card card--back" aria-label="Business card, back side">
    <div class="back__circle"></div>
    <div class="back__brand">
      <div class="back__name">VelnoriCore</div>
      <div class="back__tagline">Hardening Every Network</div>
      <div class="back__rule"></div>
      <div class="back__web">www.velnoricore-example.com</div>
    </div>
  </section>

  <section class="card card--front" aria-label="Business card, front side">
    <div class="front__head">
      <div class="brand">
        <div class="brand__dot"></div>
        <div>
          <div class="brand__name">VelnoriCore</div>
          <div class="brand__tagline">Hardening Every Network</div>
        </div>
      </div>
    </div>
    <div class="front__stripe"></div>
    <div class="front__body">
      <div class="person">
        <div class="person__name">Marten Oslow</div>
        <div class="person__title">manager</div>
      </div>
      <div class="front__web">www.<b>velnoricore-example</b>.com</div>
      <div class="divider"></div>
      <div class="contact">
        <div class="contact__company">VelnoriCore Inc.</div>
        <div>218 Larkmoor Avenue</div>
        <div>Brenton NY 10472</div>
        <div class="contact__lines">
          <div class="contact__row">
            <svg width="14" height="14" viewBox="0 0 14 14" aria-hidden="true">
              <rect x="1" y="1" width="12" height="12" rx="2" fill="#ffffff"/>
              <rect x="3" y="3" width="8" height="3" fill="#1b2f7e"/>
              <rect x="3" y="8" width="2" height="2" fill="#1b2f7e"/>
              <rect x="6" y="8" width="2" height="2" fill="#1b2f7e"/>
              <rect x="9" y="8" width="2" height="2" fill="#1b2f7e"/>
            </svg>
            <span>(555) 014-2290</span>
          </div>
          <div class="contact__row">
            <svg width="14" height="10" viewBox="0 0 14 10" aria-hidden="true">
              <rect x="0.5" y="0.5" width="13" height="9" fill="#ffffff"/>
              <path d="M0.5 0.5 L7 6 L13.5 0.5" fill="none" stroke="#1b2f7e" stroke-width="1.2"/>
            </svg>
            <span>office@velnoricore-example.com</span>
          </div>
        </div>
      </div>
    </div>
  </section>

</body>
</html>
```